Calloway Winery Wine Label Re-design

Calloway Winery is located in the Finger Lakes region of New York. The Calloway Family planted the first vineyards in 1979 and opened in 1986. We produce award winning premium, hand crafted estate grown wines. We are in the process of a wine label re-design across our entire line. We would like to have the new label 'pop' but still convey elegance and ultra-premium quality. We are open to all color and styles or a minimalist design.
The attached files contain our new logo and samples of our current label (marked current) with dimensions. Our labeler is limited to label shapes but does not necessarily to have to be die-cut(the top arch) like our current label.

Target Market(s)

Upper income quality wine drinkers

Colors

Designer to choose colors to be used in the design.

Requirements
Should not have
• Should not be a tranparent label

```html
<!DOCTYPE html>
<html lang="en">
<head>
<meta charset="utf-8">
<title>Vellanor Winery — Label Series</title>
<link href="https://fonts.googleapis.com/css2?family=Cinzel:wght@400&family=Cormorant+Garamond:wght@400&family=Montserrat:wght@400&family=Pinyon+Script&display=swap" rel="stylesheet">
<style>
  :root {
    --backdrop: #fdfaeb;
    --ink: #3a3a3a;
    --ink-soft: #6a6a6a;
    --vintage-red: #a8242e;
    --vintage-gold: #c49a2c;
    --silver-light: #fbfbfb;
    --silver-mid: #e9e9e9;
    --silver-edge: #b9b4ad;
    --cream-light: #f1edd3;
    --cream-mid: #e5e0bf;
    --cream-edge: #d6c88f;
  }
  * { margin: 0; padding: 0; box-sizing: border-box; }
  html, body {
    width: 1035px; height: 1200px; overflow: hidden;
    background: var(--backdrop);
  }
  .canvas { position: relative; width: 1035px; height: 1200px; }
  .label {
    position: absolute; top: 350px;
    width: 440px; height: 500px;
    text-align: center; color: var(--ink);
    box-shadow: 0 2px 10px rgba(0,0,0,0.08);
  }
  .label--cabernet {
    left: 50px;
    background: linear-gradient(90deg, var(--silver-mid) 0%, var(--silver-light) 30%, var(--silver-light) 55%, var(--silver-mid) 100%);
    border-bottom: 3px solid var(--silver-edge);
  }
  .label--chardonnay {
    left: 545px;
    background: linear-gradient(90deg, var(--cream-mid) 0%, var(--cream-light) 35%, var(--cream-light) 60%, var(--cream-mid) 100%);
    border-bottom: 3px solid var(--cream-edge);
  }
  .label__mark {
    position: absolute; left: 50%; top: 149px;
    width: 66px; height: 66px; margin-left: -33px;
  }
  .label__name {
    position: absolute; left: 0; right: 0; top: 252px;
    font-family: "Cinzel", serif; font-size: 36px; line-height: 1;
    letter-spacing: 0.16em; padding-left: 0.16em; color: var(--ink);
  }
  .label__sub {
    position: absolute; left: 0; right: 0; top: 291px;
    font-family: "Cinzel", serif; font-size: 13px; line-height: 1;
    letter-spacing: 0.55em; padding-left: 0.55em; color: var(--ink);
  }
  .label__tier {
    position: absolute; left: 0; right: 0; top: 318px;
    font-family: "Pinyon Script", cursive; font-size: 26px; line-height: 1;
    color: var(--ink-soft);
  }
  .label__vintage {
    position: absolute; left: 0; right: 0; top: 378px;
    font-family: "Cormorant Garamond", serif; font-style: italic;
    font-size: 17px; letter-spacing: 0.18em; line-height: 1;
  }
  .label--cabernet .label__vintage { color: var(--vintage-red); }
  .label--chardonnay .label__vintage { color: var(--vintage-gold); }
  .label__varietal {
    position: absolute; left: 0; right: 0; top: 410px;
    font-family: "Cormorant Garamond", serif; font-size: 22px;
    letter-spacing: 0.06em; line-height: 1; color: var(--ink-soft);
  }
  .label__origin {
    position: absolute; left: 0; right: 0; top: 462px;
    font-family: "Montserrat", sans-serif; font-size: 10px;
    letter-spacing: 0.2em; line-height: 1; color: var(--ink-soft);
  }
</style>
</head>
<body>
<main class="canvas">
  <section class="label label--cabernet">
    <svg class="label__mark" viewBox="0 0 66 66" aria-hidden="true">
      <circle cx="33" cy="33" r="30" fill="none" stroke="var(--ink)" stroke-width="2.5"/>
    </svg>
    <div class="label__name">VELLANOR</div>
    <div class="label__sub">WINERY</div>
    <div class="label__vintage">2013</div>
    <div class="label__varietal">CABERNET SAUVIGNON</div>
    <div class="label__origin">STATE GROWN &amp; BOTTLED</div>
  </section>

  <section class="label label--chardonnay">
    <svg class="label__mark" viewBox="0 0 66 66" aria-hidden="true">
      <circle cx="33" cy="33" r="30" fill="none" stroke="var(--ink)" stroke-width="2.5"/>
    </svg>
    <div class="label__name">VELLANOR</div>
    <div class="label__sub">WINERY</div>
    <div class="label__tier">Reserve</div>
    <div class="label__vintage">2014</div>
    <div class="label__varietal">CHARDONNAY</div>
    <div class="label__origin">STATE GROWN &amp; BOTTLED</div>
  </section>
</main>
</body>
</html>
```